Design for an annual report

Take our current design of our annual report and spice it up to make it look more professional. We are a private equity company investing in industrial companies, so we need something clean, professional, modern and stylish. Nothing B2C but very professional looking design.

- Redo the cover page
- Redo the tables and charts
- Change the font
- add a few pictures (front page picture can be changed). Stay with industrial pictures (see www.velmor-ag.ch) or swiss alps pictures.

Stay with grey, blue colors. not to many colors.

only work on it if you have real experience in designing annual repots for corporations.

Target Market(s)

financial investors in industrial companies. shareholders of our company.

most readers are 60+, Europeans, men.

Industry/Entity Type

Industrial

Font styles to use
Serif

Colors
85acd3
0455a3
eaf1f6
ceddec
c8c8c8
757575
1b1b1b
cfeae6

Requirements
Must have
• Very clean design and modern. not colorful, straight, clean, simple, professional.

See attached picture of the cover page of our corporate presentation. should use same color styles. doesnt have to be idential.
Should not have
• stay with blue shades and grey shades. Not too many colors.

```html
<!DOCTYPE html>
<html lang="de">
<head>
<meta charset="utf-8">
<title>Velmor AG – Geschäftsbericht 2013</title>
<link href="https://fonts.googleapis.com/css2?family=PT+Serif:wght@400;700&family=Source+Serif+4:wght@300;400;600;700&display=swap" rel="stylesheet">
<style>
  :root{
    --blue-dark:#0455a3;
    --navy:#1c3f7a;
    --blue-light:#85acd3;
    --ice:#eaf1f6;
    --grey-light:#c8c8c8;
    --grey:#757575;
    --ink:#1b1b1b;
    --paper:#ffffff;
    --backdrop:#ececec;
  }
  *{margin:0;padding:0;box-sizing:border-box}
  html,body{width:1200px;height:804px;overflow:hidden;background:var(--backdrop)}
  .canvas{position:relative;width:1200px;height:804px}
  .spread{position:absolute;left:77px;top:32px;width:1046px;height:740px;display:flex;box-shadow:0 6px 24px rgba(0,0,0,.18)}
  .page{position:relative;width:523px;height:740px;background:var(--paper);overflow:hidden}
  .page--left{background:linear-gradient(to right,#fff 85%,#ececec)}
  .page--right{background:linear-gradient(to left,#fff 88%,#ececec)}
  .page-edge{position:absolute;top:0;left:0;right:0;height:10px;background:var(--grey-light)}
  .folio{position:absolute;top:14px;font:400 9px "PT Serif",serif;color:var(--grey)}
  .folio--left{left:26px}
  .folio--right{right:26px}
  .folio-tab{position:absolute;top:10px;width:14px;height:4px;background:var(--navy)}
  .page--left .folio-tab{left:22px}
  .page--right .folio-tab{right:22px}
  .band{position:absolute;left:30px;right:0;top:44px;height:30px;background:var(--navy)}
  .toc-heading{position:absolute;left:48px;top:150px}
  .toc-heading h1{font:700 21px "Source Serif 4",serif;color:var(--navy);letter-spacing:.6px}
  .toc-heading p{font:300 18px "Source Serif 4",serif;color:var(--grey);margin-top:2px}
  .toc{position:absolute;left:62px;top:258px;width:290px;list-style:none}
  .toc li{display:flex;justify-content:space-between;align-items:flex-end;border-bottom:1px solid var(--grey);padding:8px 0 2px;font:400 8.5px "PT Serif",serif;color:var(--grey)}
  .toc li span:last-child{color:var(--ink)}
  .decor{position:absolute;left:0;top:0}
  .letter-title{position:absolute;left:46px;top:110px;font:700 23px "Source Serif 4",serif;color:#3a3a3a}
  .columns{position:absolute;left:46px;top:166px;width:444px;display:flex;gap:26px}
  .column{flex:1;font:400 7.4px/1.5 "PT Serif",serif;color:#3a3a3a}
  .column p{margin-bottom:9px}
  .subhead{font:700 9.5px "Source Serif 4",serif;color:var(--blue-dark);margin:8px 0 6px;letter-spacing:.3px}
  .binding{position:absolute;width:4px;height:10px;background:var(--grey-light);border-radius:2px}
</style>
</head>
<body>
<div class="canvas">
  <div class="spread">
    <section class="page page--left">
      <div class="page-edge"></div>
      <div class="folio-tab"></div>
      <span class="folio folio--left">2</span>
      <div class="band"></div>
      <div class="toc-heading">
        <h1>INHALTSVERZEICHNIS</h1>
        <p>Inhalt</p>
      </div>
      <svg class="decor" width="523" height="740" viewBox="0 0 523 740" aria-hidden="true">
        <line x1="40" y1="240" x2="470" y2="240" stroke="var(--grey-light)" stroke-width="1"/>
        <line x1="30" y1="460" x2="500" y2="460" stroke="var(--grey-light)" stroke-width="1"/>
      </svg>
      <ul class="toc">
        <li><span>An unsere Aktionäre</span><span>3</span></li>
        <li><span>Der Velmor Konzern</span><span>4</span></li>
        <li><span>Kennzahlen der Velmor AG</span><span>5</span></li>
        <li><span>Informationen zu den Portfoliofirmen</span><span>6</span></li>
        <li><span>Anlagegrundsätze und Corporate Governance</span><span>7</span></li>
      </ul>
    </section>
    <section class="page page--right">
      <div class="page-edge"></div>
      <div class="folio-tab"></div>
      <span class="folio folio--right">3</span>
      <div class="binding" style="top:90px;left:0"></div>
      <h2 class="letter-title">An unsere Aktionäre</h2>
      <div class="columns">
        <div class="column">
          <p>Sehr geehrte Aktionäre,</p>
          <p>Das zurückliegende Jahr ging zu Ende. Vieles haben wir erreicht, einige Projekte dauerten länger als ursprünglich geplant, und einige Themen konnten wir noch nicht zufriedenstellend abschliessen. Insgesamt hat Velmor ein erfolgreiches Jahr hinter sich, welches wir Ihnen mit diesem Geschäftsbericht gerne näher bringen möchten. Im 2013 wurde die Velmor AG zum ersten Mal mit Kapital ausgestattet und hat seither zwei erfolgreiche industrielle Unternehmen erworben und diese erfolgreich integriert.</p>
          <h3 class="subhead">STRATEGISCHE HIGHLIGHTS</h3>
          <p>Kurz vor Weihnachten 2013 haben wir die Keller Maschinen und Pumpen AG („Keller AG“) übernommen. Wie geplant konnten wir am 21. Januar 2013 den Kauf der Hofer Elektronik AG und ihrer Tochtergesellschaften („Hofer“) erfolgreich abschliessen. Der Kauf von zwei Unternehmen innerhalb 4 Wochen war für uns alle eine Herausforderung. Rückblickend können wir festhalten, dass wir bei beiden Unternehmen eine Due Diligence mit der notwendigen Sorgfalt durchgeführt haben und alle wichtigen Risiken erkannt haben.</p>
        </div>
        <div class="column">
          <p>Sofort nach der Übernahme ging es an die Umsetzung der jeweiligen 100-Tage Pläne. Hier galt es primär darum, die Führung zu übernehmen und den Mitarbeitern in der Zeit der Unsicherheit Perspektiven zu bieten. Der Wechsel der ehemaligen Besitzer/Unternehmer in der Firma führte zu einer anspruchsvollen Führungssituation, die wir aber insgesamt gut gemeistert haben. Bei beiden Firmen haben wir rasch ein detailliertes operatives Monatscontrolling eingeführt, welches auf die Schlüsselgrössen fokussiert.</p>
          <p>Für beide Unternehmen konnten wir sehr attraktive Akquisitionsfinanzierungen verhandeln, welche wir bereits begonnen haben zu amortisieren.</p>
          <p>Insgesamt haben sich die zwei Unternehmen ansprechend entwickelt. Details zu den zwei Unternehmen sind weiter unten aufgeführt.</p>
          <p>Im Juli 2013 konnten wir mit Hans-Ulrich Brändli einen weiteren Aktionär für Velmor begeistern, weshalb wir eine kleine Kapitalerhöhung durchgeführt haben. Eine zweite Kapitalerhöhung im Umfang von CHF xx Mio. von bisherigen xx Aktionären haben wir am 4. Dezember 2013 erfolgreich abgeschlossen.</p>
        </div>
      </div>
    </section>
  </div>
</div>
</body>
</html>
```